Business card - mobile service

O KiraVox is a mobile family safety service based on tablets and smartphones.
The business card must have:
BASIC INFO
Company Logo
Name
Position / Job Title: Co-founder
Mobile Phone Number: +55 (11) 5830 9172
Land Line: +55 (11) 8761 203945
Email Address: name@kiravox-example.com
Web Site URL: www.kiravox-example.com
PROMOTIONAL INFO
Try KiraVox free Today!
Your personal promo code: qqqq-5839-wwww-4162-9087
Promo code text explanation with the instructions about the trial offer
Updates
Dears,
One more must have: the KiraVox slogan:
Safety

```html
<!DOCTYPE html>
<html lang="en">
<head>
<meta charset="utf-8">
<title>KiraVox business card</title>
<link rel="stylesheet" href="https://fonts.googleapis.com/css2?family=Open+Sans:wght@400;600;700&display=swap">
<style>
  :root {
    --backdrop: #e4e4e4;
    --card-white: #ffffff;
    --brand-blue: #2ba8e2;
    --accent-orange: #f5a623;
    --ink: #2b2b2b;
    --divider: #8a8a8a;
    --on-blue: #ffffff;
    --on-blue-soft: #eaf6fd;
  }
  * { box-sizing: border-box; margin: 0; padding: 0; }
  html, body {
    width: 1200px; height: 900px; overflow: hidden;
    background: var(--backdrop);
    font-family: "Open Sans", Arial, sans-serif;
  }
  .canvas { position: relative; width: 1200px; height: 900px; }

  .card {
    position: absolute;
    width: 500px; height: 286px;
    box-shadow: 0 3px 8px rgba(0,0,0,0.25);
  }

  /* Front side */
  .card-front {
    left: 80px; top: 206px;
    background: var(--card-white);
    border-top-right-radius: 44px;
  }
  .front-brand {
    position: absolute; left: 44px; top: 68px;
    display: flex; align-items: center; gap: 8px;
  }
  .brand-name {
    font-weight: 700; font-size: 40px; letter-spacing: -0.5px;
    color: var(--brand-blue); line-height: 1;
  }
  .brand-dot {
    width: 14px; height: 14px; border-radius: 50%;
    background: var(--accent-orange);
  }
  .front-divider {
    position: absolute; left: 250px; top: 60px;
    width: 1px; height: 160px; background: var(--divider);
  }
  .contact-block {
    position: absolute; left: 272px; top: 60px;
    color: var(--ink);
  }
  .person-name {
    font-weight: 700; font-size: 22px; color: var(--brand-blue); line-height: 1.2;
  }
  .person-role { font-size: 15px; line-height: 1.3; margin-bottom: 20px; }
  .contact-list { list-style: none; font-size: 14px; line-height: 22px; }
  .contact-label { color: var(--accent-orange); display: inline-block; width: 14px; }
  .web-url { font-size: 14px; margin-top: 8px; }

  /* Back side */
  .card-back {
    left: 630px; top: 410px;
    background: var(--brand-blue);
    border-top-left-radius: 44px;
    color: var(--on-blue);
    text-align: center;
  }
  .back-brand {
    position: absolute; left: 0; right: 0; top: 42px;
    display: flex; justify-content: center; align-items: center; gap: 8px;
  }
  .back-brand .brand-name { color: var(--on-blue); font-size: 44px; }
  .back-brand .brand-dot { background: var(--on-blue); }
  .slogan {
    position: absolute; left: 0; right: 0; top: 104px;
    font-weight: 600; font-size: 18px;
  }
  .promo {
    position: absolute; left: 0; right: 0; top: 172px;
    color: var(--on-blue-soft);
  }
  .promo-title { font-weight: 700; font-size: 15px; color: var(--on-blue); margin-bottom: 4px; }
  .promo-text { font-size: 12.5px; line-height: 20px; }
</style>
</head>
<body>
<main class="canvas">
  <section class="card card-front" aria-label="Card front">
    <div class="front-brand">
      <span class="brand-name">kiravox</span>
      <span class="brand-dot"></span>
    </div>
    <div class="front-divider"></div>
    <div class="contact-block">
      <p class="person-name">Kira Lune</p>
      <p class="person-role">Co-founder</p>
      <ul class="contact-list">
        <li><span class="contact-label">M</span>+55 (11) 5830 9172</li>
        <li><span class="contact-label">T</span>+55 (11) 8761 203945</li>
        <li><span class="contact-label">E</span>name@kiravox-example.com</li>
      </ul>
      <p class="web-url">www.kiravox-example.com</p>
    </div>
  </section>

  <section class="card card-back" aria-label="Card back">
    <div class="back-brand">
      <span class="brand-name">kiravox</span>
      <span class="brand-dot"></span>
    </div>
    <p class="slogan">Your Family Safety Service</p>
    <div class="promo">
      <p class="promo-title">Try KiraVox free Today!</p>
      <p class="promo-text">Your personal promo code: qqqq-5839-wwww-4162-9087<br>
      Promo code text explanation with the instructions<br>
      about the trial offer.</p>
    </div>
  </section>
</main>
</body>
</html>
```